Gift Voucher For Medical Cosmetic Clinic

I need a high end, beautiful gift voucher for my Cosmetic Medical Clinic that I will provide to customers in a beautifully designed envelope. I like the colours blue with different tones of blue, white and silver. I have attached my business card for further information.
The address is: 3/14 Dunmore Lane, Ferrymead, Christchurch 8023.
Phone: 0800-457-839
Email: mirel@tovanu.co.nz
Website: www.tovanu.co.nz

```html
<!DOCTYPE html>
<html lang="en">
<head>
<meta charset="utf-8">
<title>Tovanu Gift Voucher</title>
<link rel="stylesheet" href="https://fonts.googleapis.com/css2?family=Quicksand:wght@300;400&display=swap">
<style>
  :root {
    --paper-light: #f7f8fa;
    --paper-edge: #d9dde1;
    --slate: #8a9aa2;
    --slate-dark: #7b8a92;
    --label-box: #87979e;
    --ribbon-deep: #1f6ff0;
    --ribbon-mid: #4a96f7;
    --ribbon-glow: #9ef0fb;
    --service-blue: #4a8df0;
    --silver-light: #e4e8eb;
    --silver-mid: #a7b1b8;
    --silver-dark: #6d7880;
  }
  * { margin: 0; padding: 0; box-sizing: border-box; }
  html, body { width: 1200px; height: 566px; overflow: hidden; background: #ffffff; }
  .voucher {
    position: relative;
    width: 1200px;
    height: 566px;
    overflow: hidden;
    font-family: "Quicksand", sans-serif;
    background: radial-gradient(ellipse 70% 80% at 45% 45%, var(--paper-light) 0%, #eceff2 60%, var(--paper-edge) 100%);
  }
  .bokeh-glow {
    position: absolute;
    border-radius: 50%;
    background: radial-gradient(circle, rgba(200,208,216,0.55) 0%, rgba(220,226,232,0.25) 55%, rgba(255,255,255,0) 75%);
  }
  .bokeh-glow--right { left: 860px; top: 0; width: 420px; height: 566px; }
  .bokeh-glow--left { left: 200px; top: 150px; width: 260px; height: 320px; }
  .name-plate {
    position: absolute;
    left: 60px; top: 60px;
    width: 297px; height: 81px;
    background: var(--label-box);
  }
  .ribbon { position: absolute; }
  .ribbon--horizontal {
    left: 0; top: 317px;
    width: 1200px; height: 47px;
    background: linear-gradient(90deg, var(--ribbon-deep) 0%, var(--ribbon-mid) 35%, var(--ribbon-glow) 58%, var(--ribbon-mid) 70%, var(--ribbon-deep) 80%, var(--ribbon-mid) 100%);
    box-shadow: 0 6px 10px rgba(60,70,80,0.18);
  }
  .ribbon--vertical {
    left: 834px; top: 0;
    width: 45px; height: 566px;
    background: linear-gradient(180deg, var(--ribbon-deep) 0%, var(--ribbon-mid) 45%, #7fc3fa 58%, var(--ribbon-mid) 75%, var(--ribbon-deep) 100%);
    box-shadow: 5px 0 10px rgba(60,70,80,0.16);
  }
  .bow {
    position: absolute;
    left: 740px; top: 228px;
    width: 232px; height: 222px;
    border-radius: 50%;
    background: radial-gradient(circle at 45% 40%, var(--silver-light) 0%, var(--silver-mid) 55%, var(--silver-dark) 100%);
    box-shadow: 4px 8px 14px rgba(40,50,60,0.3);
  }
  .title-gift {
    position: absolute;
    left: 368px; top: 100px;
    font-size: 232px;
    font-weight: 300;
    line-height: 1;
    letter-spacing: -6px;
    color: var(--slate);
  }
  .title-voucher {
    position: absolute;
    left: 553px; top: 368px;
    font-size: 46px;
    font-weight: 300;
    color: var(--slate);
  }
  .contact {
    position: absolute;
    left: 922px; top: 60px;
    list-style: none;
    font-size: 16px;
    letter-spacing: 1.6px;
    color: var(--slate);
    line-height: 19.5px;
  }
  .contact li { display: flex; margin-bottom: 4px; }
  .contact__label { width: 36px; flex: none; }
  .tagline {
    position: absolute;
    left: 58px; top: 440px;
    font-size: 21px;
    font-weight: 400;
    color: var(--slate-dark);
    letter-spacing: 0.3px;
  }
  .services {
    position: absolute;
    left: 58px; top: 487px;
    font-size: 17px;
    color: var(--service-blue);
    letter-spacing: 0.2px;
    white-space: nowrap;
  }
  .services__sep { color: var(--slate); margin: 0 6px; font-size: 12px; }
</style>
</head>
<body>
  <main class="voucher">
    <div class="bokeh-glow bokeh-glow--left" role="img" aria-label="Soft blurred bokeh light circles"></div>
    <div class="bokeh-glow bokeh-glow--right" role="img" aria-label="Soft blurred bokeh light circles"></div>

    <div class="name-plate"></div>

    <div class="ribbon ribbon--horizontal"></div>
    <div class="ribbon ribbon--vertical"></div>

    <div class="title-gift">gift</div>
    <div class="title-voucher">voucher</div>

    <div class="bow" role="img" aria-label="Silver gift bow where the ribbons cross"></div>

    <ul class="contact">
      <li><span class="contact__label">a ::</span><span>3/14 Dunmore Lane,<br>Ferrymead,<br>Christchurch 8023</span></li>
      <li><span class="contact__label">p ::</span><span>0800-457-839</span></li>
      <li><span class="contact__label">e ::</span><span>mirel@tovanu.co.nz</span></li>
      <li><span class="contact__label">w ::</span><span>www.tovanu.co.nz</span></li>
    </ul>

    <p class="tagline">TOVANU - YOUR LOCAL COSMETIC CLINIC</p>
    <p class="services">dermal injectables<span class="services__sep">::</span>plasma facials<span class="services__sep">::</span>microneedling<span class="services__sep">::</span>skin boosters<span class="services__sep">::</span>excessive sweating</p>
  </main>
</body>
</html>
```